BRIMLOW Pizza and Wraps

We need a website for a new restaurant called BRIMLOW "PIZZA AND WRAPS".
I have attached fonts, background images, logo, images, content etc.
can provide you with what you need to get the website design done fast and easy

I have uploaded more images of the venue and some menu items. let me know if there is anything I need to provide to make your mission clear and easy

Reason: i would like a little time to provide more feedback to designers

Industry/Entity Type

Restaurant

Coding

Coded - Design and coding required

Number of Pages Required

5+ page

Colors

Designer to choose colors to be used in the design.

Requirements
Must have
• PAGES:
• Our Story
• Menu
• Reservations
• Catering & Delivery
• Contact

```html
<!DOCTYPE html>
<html lang="en">
<head>
<meta charset="utf-8">
<title>BRIMLOW Pizza and Wraps</title>
<link rel="stylesheet" href="https://fonts.googleapis.com/css2?family=Open+Sans:ital,wght@0,400;0,600;0,700;1,400&family=Yanone+Kaffeesatz:wght@300;400;600;700&display=swap">
<style>
:root{
  --red:#ec1c24;
  --red-dark:#b5121a;
  --ink:#222;
  --text:#555;
  --muted:#888;
  --grey-panel:#dcdcdc;
  --footer:#2b2b2b;
  --yellow:#f5c400;
  --white:#fff;
}
*{box-sizing:border-box;margin:0;padding:0}
html,body{width:1200px;height:2338px;overflow:hidden;background:var(--white)}
body{position:relative;font-family:"Open Sans",Arial,sans-serif;color:var(--text)}
.abs{position:absolute}

/* header */
.site-header{position:absolute;left:0;top:0;width:1200px;height:93px;background:var(--white)}
.brand{position:absolute;left:234px;top:26px;font-family:"Yanone Kaffeesatz",sans-serif;font-weight:700;font-size:40px;color:var(--red);letter-spacing:1px;line-height:1}
.main-nav{position:absolute;left:392px;top:36px;display:flex;gap:33px;font-size:11px;color:var(--red)}
.call{position:absolute;left:824px;top:24px;color:var(--red)}
.call small{display:flex;align-items:center;gap:5px;font-size:9px;color:#d4a100}
.call strong{display:block;font-size:19px;font-weight:700;margin-top:2px;letter-spacing:.5px}

/* category bar */
.category-bar{position:absolute;left:0;top:93px;width:1200px;height:53px;background:var(--red);display:flex;justify-content:center;gap:30px;align-items:center}
.category{display:flex;align-items:center;gap:10px;color:var(--white);font-size:11.5px;width:90px}
.category.active{font-weight:700}
.category svg{width:26px;height:26px;stroke:var(--white);fill:none;stroke-width:1.6}

/* hero */
.hero{position:absolute;left:0;top:146px;width:1200px;height:282px;background:linear-gradient(90deg,#111 0%,#2a2a2a 30%,#3a3a3a 60%,#2c2c2c 100%)}
.hero-veg{position:absolute;left:200px;top:0;width:250px;height:282px;background:radial-gradient(circle at 40% 45%,#a0241f 0%,#4a6e1f 40%,#141414 80%)}
.hero-pizza{position:absolute;left:490px;top:16px;width:250px;height:250px;border-radius:50%;background:radial-gradient(circle,#d98a2c 0%,#b75a1d 55%,#8a3e12 75%,#c98f45 100%)}
.hero-offer{position:absolute;left:758px;top:50px;width:260px;text-align:center;font-family:"Yanone Kaffeesatz",sans-serif;color:#eee}
.badge-new{position:absolute;left:6px;top:0;width:38px;height:38px;border-radius:50%;background:var(--red);color:var(--white);font-size:13px;font-weight:700;font-style:italic;display:flex;align-items:center;justify-content:center}
.offer-kicker{font-size:22px;color:var(--yellow);font-style:italic;margin-left:30px;padding-top:10px}
.offer-title{font-size:46px;line-height:.95;font-style:italic;margin-top:4px}
.offer-title em{color:var(--red);font-style:italic}
.offer-tags{display:inline-block;margin-top:12px;background:var(--red);color:var(--white);font-size:12px;padding:7px 12px;font-style:italic}
.hero-strip{position:absolute;left:0;top:428px;width:1200px;height:8px;background:var(--red)}
.divider-shadow{position:absolute;left:210px;top:458px;width:280px;height:6px;background:radial-gradient(ellipse at center,rgba(0,0,0,.12) 0%,rgba(0,0,0,0) 70%)}

/* about */
.about{position:absolute;left:0;top:492px;width:1200px;height:294px}
.about-red{position:absolute;left:0;top:0;width:234px;height:294px;background:var(--red)}
.about-photo{position:absolute;left:234px;top:0;width:222px;height:294px;background:linear-gradient(160deg,#b26a4c 0%,#6d3a2a 45%,#2d2a24 75%,#4c5a38 100%)}
.about-edge{position:absolute;left:456px;top:0;width:44px;height:294px;background:linear-gradient(90deg,var(--red-dark) 0 30%,var(--red) 30% 100%)}
.about-panel{position:absolute;left:500px;top:0;width:700px;height:294px;background:var(--grey-panel);padding:40px 28px}
.about-panel h2{font-family:"Yanone Kaffeesatz",sans-serif;font-weight:600;font-size:20px;color:#444;letter-spacing:.5px}
.about-panel p{font-family:"Yanone Kaffeesatz",sans-serif;font-size:14px;line-height:24px;color:#666;margin-top:12px;width:450px}

/* section titles */
.section-title{position:absolute;left:0;width:1200px;text-align:center;font-family:"Yanone Kaffeesatz",sans-serif;font-weight:700;font-size:24px;color:var(--ink)}
.section-title::after{content:"";display:block;width:74px;height:2px;background:var(--red);margin:6px auto 0}

/* features */
.features{position:absolute;left:225px;top:908px;width:750px;display:flex;justify-content:space-between}
.feature{width:140px;text-align:center}
.feature svg{width:62px;height:56px;stroke:#777;fill:none;stroke-width:1.3}
.feature h3{font-size:12px;font-weight:400;color:#333;margin-top:26px}
.feature p{font-size:9px;line-height:14px;color:var(--muted);margin-top:4px}

/* pizza of the day */
.deal{position:absolute;left:0;top:1084px;width:1200px;height:293px;background:radial-gradient(ellipse at 55% 50%,#5a4640 0%,#3d3532 55%,#2b2a29 100%)}
.deal-inner{position:absolute;left:0;top:60px;width:1200px;text-align:center;font-family:"Yanone Kaffeesatz",sans-serif;color:var(--white)}
.deal-kicker{font-size:15px;letter-spacing:1px;color:#ddd;display:flex;justify-content:center;align-items:center;gap:8px}
.deal-kicker::before,.deal-kicker::after{content:"";width:60px;height:1px;background:#ccc}
.deal-title{font-size:46px;font-weight:700;line-height:1;margin-top:2px}
.deal-price{display:flex;justify-content:center;align-items:flex-start;gap:4px;margin-top:4px;margin-left:60px}
.deal-price .amt{font-size:58px;font-weight:700;line-height:.9}
.deal-price sup{font-size:26px;font-weight:700}
.deal-price small{font-size:10px;color:var(--yellow);display:block}
.deal-list{text-align:left;font-size:12px;color:var(--yellow);line-height:17px;margin-left:6px;margin-top:6px}
.btn{display:inline-flex;align-items:center;justify-content:center;gap:8px;background:var(--red);color:var(--white);font-family:"Open Sans",sans-serif;font-weight:700;font-size:10px}
.deal .btn{width:132px;height:34px;margin-top:20px}

/* pizza sets */
.sets-rule{position:absolute;left:228px;top:1410px;width:744px;height:1px;background:#eee}
.cards{position:absolute;left:228px;top:1502px;width:726px;display:flex;justify-content:space-between}
.card{width:226px;height:438px;text-align:center;position:relative}
.card.featured{border:1px solid #ddd;box-shadow:0 0 4px rgba(0,0,0,.15);background:var(--white)}
.card-image{width:224px;height:200px;margin:0 auto}
.card h3{font-size:14px;font-weight:400;color:var(--ink);margin-top:14px}
.card p{font-size:8.5px;font-style:italic;line-height:14px;color:var(--muted);margin:8px auto 0;width:180px}
.size-label{font-size:8px;color:#333;margin:22px auto 0;width:190px;display:flex;align-items:center;gap:8px}
.size-label::before,.size-label::after{content:"";flex:1;height:1px;background:#e6e6e6}
.sizes{display:flex;justify-content:center;gap:18px;margin-top:14px;font-size:13px;color:#333}
.size{display:flex;align-items:center;gap:6px}
.size i{width:28px;height:28px;border-radius:50%;border:1px solid #eee;font-style:normal;font-size:7px;font-weight:700;line-height:9px;display:flex;flex-direction:column;align-items:center;justify-content:center}
.size i.on{background:var(--yellow);border-color:var(--yellow)}
.size sup{font-size:8px}
.card .btn{width:154px;height:34px;border-radius:17px;margin-top:20px}

/* footer */
.site-footer{position:absolute;left:0;top:2028px;width:1200px;height:310px;background:var(--footer);text-align:center}
.socials{position:absolute;left:0;top:55px;width:1200px;display:flex;justify-content:center;gap:17px}
.socials span{width:32px;height:32px;border-radius:50%;border:1.5px solid #666}
.footer-brand{position:absolute;left:0;top:115px;width:1200px;font-family:"Yanone Kaffeesatz",sans-serif;font-weight:700;font-size:34px;color:var(--red-dark);letter-spacing:1px}
.footer-info{position:absolute;left:0;top:198px;width:1200px;display:flex;justify-content:center;gap:14px;font-size:8.5px;color:#eee}
.footer-info span+span::before{content:"|";color:#666;margin-right:14px}
.copyright{position:absolute;left:0;top:218px;width:1200px;font-size:7.5px;color:#888}
.map-btn{position:absolute;left:529px;top:272px;width:142px;height:38px;border-radius:8px 8px 0 0}
</style>
</head>
<body>

<header class="site-header">
  <div class="brand">BRIMLOW</div>
  <nav class="main-nav">
    <span>Order Online</span><span>About</span><span>Menu</span><span>Reservation</span><span>Events &amp; Delivery</span>
  </nav>
  <div class="call">
    <small><svg width="10" height="10" viewBox="0 0 24 24" fill="#ec1c24"><path d="M6.6 10.8a15 15 0 006.6 6.6l2.2-2.2c.3-.3.7-.4 1-.2 1.1.4 2.3.6 3.6.6.6 0 1 .4 1 1V20c0 .6-.4 1-1 1A17 17 0 013 4c0-.6.4-1 1-1h3.5c.6 0 1 .4 1 1 0 1.3.2 2.5.6 3.6.1.3 0 .7-.2 1z"/></svg>Call and Order in</small>
    <strong>55 010 224 318</strong>
  </div>
</header>

<nav class="category-bar">
  <div class="category active"><svg viewBox="0 0 26 26"><path d="M3 23L12 3l11 20z"/><circle cx="12" cy="15" r="1.5"/><circle cx="15" cy="19" r="1.2"/></svg>Pizza</div>
  <div class="category"><svg viewBox="0 0 26 26"><path d="M3 11a10 7 0 0120 0z"/><path d="M3 14h20M3 17h20"/><path d="M4 20h18v2H4z"/></svg>Burgers</div>
  <div class="category"><svg viewBox="0 0 26 26"><path d="M2 13h22a11 9 0 01-22 0z"/><path d="M7 13c0-4 3-6 6-6s6 2 6 6"/></svg>Salads</div>
  <div class="category"><svg viewBox="0 0 26 26"><path d="M2 20a11 12 0 0122 0z"/><path d="M6 16h2M11 13h2M16 16h2"/></svg>Tacos</div>
  <div class="category"><svg viewBox="0 0 26 26"><path d="M7 3h12l-2 20H9z"/><path d="M7 9h12"/></svg>Wraps</div>
  <div class="category"><svg viewBox="0 0 26 26"><path d="M6 12h14l-2 11H8z"/><path d="M8 12V4M11 12V3M14 12V4M17 12V5"/></svg>Fries</div>
  <div class="category"><svg viewBox="0 0 26 26"><path d="M2 13h22a11 9 0 01-22 0z"/><path d="M7 13c0-4 3-6 6-6s6 2 6 6"/></svg>Salads</div>
  <div class="category"><svg viewBox="0 0 26 26"><path d="M9 7h8v16H9z"/><path d="M11 7V3h4v4"/></svg>Drinks</div>
</nav>

<section class="hero">
  <div class="hero-veg" role="img" aria-label="Fresh peppers, tomatoes and vegetables on a dark stone surface"></div>
  <div class="hero-pizza" role="img" aria-label="Whole pizza topped with mushrooms and peppers"></div>
  <div class="hero-offer">
    <div class="badge-new">NEW!</div>
    <div class="offer-kicker">Limitted Time Offer</div>
    <div class="offer-title">Get <em>2</em> Medium<br>Pizzas at <em>$5</em></div>
    <div class="offer-tags">Bacon · Grilled Onions · Potatos · Mozzarella · BBQ Sauce</div>
  </div>
</section>
<div class="hero-strip"></div>
<div class="divider-shadow"></div>

<section class="about">
  <div class="about-red"></div>
  <div class="about-photo" role="img" aria-label="Restaurant entrance with brick wall and plants"></div>
  <div class="about-edge"></div>
  <div class="about-panel">
    <h2>ABOUT US</h2>
    <p>Rich in heritage, BRIMLOW is a gathering place celebrating the Mediterranean's finest Produce.<br>
    BRIMLOW is the ultimate escape – the perfect spot to enjoy sensational food and drinks that showcases everything the Mediterranean has to offer in a single, sophisticated setting.<br>
    Where an early morning walk to the bakery around the corner is a way of life, nothing beats the first batch of bread from the oven to start your day. So we combined a variety of best ingredients and delicacies for you to enjoy that experiencewhenever you got the urge to do so</p>
  </div>
</section>

<h2 class="section-title" style="top:840px">Features</h2>
<section class="features">
  <div class="feature">
    <svg viewBox="0 0 62 56"><path d="M10 26h42l-5 22H15z"/><path d="M18 26l8-16M44 26l-8-16"/><path d="M14 34h34M16 41h30"/></svg>
    <h3>Best Quality</h3><p>Praesent pulvinar neque pel-<br>lentesque mattis pretium.</p>
  </div>
  <div class="feature">
    <svg viewBox="0 0 62 56"><circle cx="34" cy="30" r="17"/><path d="M34 20v10l7 5"/><path d="M30 10h8M6 24h12M4 31h12M8 38h10"/></svg>
    <h3>On Time</h3><p>Praesent pulvinar neque pel-<br>lentesque mattis pretium.</p>
  </div>
  <div class="feature">
    <svg viewBox="0 0 62 56"><path d="M20 30a9 9 0 01-1-17 11 11 0 0124-1 9 9 0 011 18z"/><path d="M22 30v8h18v-8"/><path d="M31 44v8M25 48h12"/></svg>
    <h3>MasterChefs</h3><p>Praesent pulvinar neque pel-<br>lentesque mattis pretium.</p>
  </div>
  <div class="feature">
    <svg viewBox="0 0 62 56"><path d="M8 42a23 23 0 0146 0z"/><path d="M4 46h54"/><circle cx="31" cy="17" r="2.5"/><path d="M24 32c2-3 0-5 2-8M31 32c2-3 0-5 2-8M38 32c2-3 0-5 2-8"/></svg>
    <h3>Taste Food</h3><p>Praesent pulvinar neque pel-<br>lentesque mattis pretium.</p>
  </div>
</section>

<section class="deal" role="img" aria-label="Close-up of a tomato and basil pizza, darkened">
  <div class="deal-inner">
    <div class="deal-kicker">FREE DELIVERY WITH</div>
    <div class="deal-title">PIZZA OF THE DAY</div>
    <div class="deal-price">
      <sup>$</sup><span class="amt">9</span><div><sup>99</sup><small>EACH</small></div>
      <div class="deal-list">- VEGGIE LOVER<br>- HAWAII<br>- SUPREME</div>
    </div>
    <span class="btn">Order Now</span>
  </div>
</section>

<div class="sets-rule"></div>
<h2 class="section-title" style="top:1418px">Pizza Sets</h2>

<section class="cards">
  <article class="card">
    <div class="card-image" role="img" aria-label="Caesar salad with bacon and greens" style="background:linear-gradient(150deg,#5e7a2c 0%,#8c3a22 45%,#c9a878 80%,#e9e2cf 100%)"></div>
    <h3>Caeser Salad</h3>
    <p>Ricotta, sun dried tomatoes, garlic, mozza-rella cheese, topped with lightly drizzled red sauce, pesto, and fresh basil</p>
    <div class="size-label">Pick Size</div>
    <div class="sizes">
      <div class="size"><i>22<br>cm</i><span><sup>$</sup>19.90</span></div>
      <div class="size"><i>29<br>cm</i><span><sup>$</sup>25.90</span></div>
    </div>
  </article>
  <article class="card featured">
    <div class="card-image" role="img" aria-label="Grilled halloumi slices on a plate" style="width:224px;background:linear-gradient(180deg,#e7b45a 0%,#f4d28c 50%,#d89a3c 78%,#cfcfcf 80%,#cfcfcf 100%)"></div>
    <h3>Halloami</h3>
    <p>Extra-virgin olive oil, garlic, mozzarella cheese, onions, mushrooms, green olives, black olives, fresh tomatoes</p>
    <div class="size-label">Pick Size</div>
    <div class="sizes">
      <div class="size"><i class="on">22<br>cm</i><span><sup>$</sup>19.90</span></div>
      <div class="size"><i>29<br>cm</i><span><sup>$</sup>25.90</span></div>
    </div>
    <span class="btn"><svg width="12" height="12" viewBox="0 0 12 12" fill="none" stroke="#fff" stroke-width="1.3"><path d="M2 4h8l-1 7H3z"/><path d="M4 4V2.5a2 2 0 014 0V4"/></svg>Add to Cart</span>
  </article>
  <article class="card">
    <div class="card-image" role="img" aria-label="Bowl of hummus with olive oil and chickpeas" style="background:radial-gradient(circle at 50% 45%,#c8a12a 0%,#e6d3a6 30%,#eedfbd 55%,#f6efe0 75%,#8a5a3a 100%)"></div>
    <h3>Hummus</h3>
    <p>Extra-virgin olive oil, mozzarella cheese, thinly-sliced steak meat, garlic, green pep-pers, mushrooms and tomatoes</p>
    <div class="size-label">Pick Size</div>
    <div class="sizes">
      <div class="size"><i>22<br>cm</i><span><sup>$</sup>19.90</span></div>
      <div class="size"><i>29<br>cm</i><span><sup>$</sup>25.90</span></div>
    </div>
  </article>
</section>

<footer class="site-footer">
  <div class="socials"><span></span><span></span><span></span><span></span><span></span></div>
  <div class="footer-brand">BRIMLOW</div>
  <div class="footer-info">
    <span>BRIMLOW Pizza and Wraps</span><span>Address Line</span><span>Telephone: +0 000 0000</span><span>Fax: +0 000 0000</span>
  </div>
  <div class="copyright">Copyright © 2016. All rights reserved.</div>
  <span class="btn map-btn"><svg width="12" height="14" viewBox="0 0 12 14" fill="none" stroke="#fff" stroke-width="1.3"><path d="M6 13s5-5 5-8a5 5 0 00-10 0c0 3 5 8 5 8z"/><circle cx="6" cy="5" r="1.6"/></svg>Find us on Map</span>
</footer>

</body>
</html>
```